I need a compelling, relevant cover for a book being published in January - title is the name of this project. The book is a call to action to women to become entrepreneurs as today's best path to achieving parity, purpose, prosperity and passion. See extended description of the book's message online at:
walkingtallneverrequireswalkingalone.example
(and attached pdf -- the cover art posted here is simply a placeholder/clip art ). I'm looking for something more emotional and exciting and distinctive and appropriate to the subject matter and message..
type on cover must include:
Standing Tall Won't Require Standing Alone
By Marcia T. Vellby
How Trusting Your Own Instincts Can Shift Your Path and Build Your Venture
With a Foreword by CEO Dorinda P. Halvorsen

Target Market(s)

Professional women, women business owners, aspiring women students, marketers who target women in business, such as IT providers; lenders and funders; financial services like credit card issuers -- anyone who sells to women i biz. Women's networking groups,entrepreneurship divisions at universities, and associations. International audience but tilted toward US readers.

Industry/Entity Type

Call

Font styles to use
Serif

Requirements
Nice to have
• Something that stands out from the crowd -- that would make a woman want to pick up the book because it "speaks" her language/values. Something that addresses contemporary, up-to-date ideas about gender equity/sex roles/women's advancement
Should not have
• NOTHING PINK! Please avoid "empowerment" looks and ideas (too cliche) and avoid traditional business images, like briefcases

```html
<!DOCTYPE html>
<html lang="en">
<head>
<meta charset="UTF-8">
<title>Standing Tall Won't Require Standing Alone — Book Cover</title>
<link href="https://fonts.googleapis.com/css2?family=Alfa+Slab+One&family=Source+Sans+3:wght@400;600&family=Dancing+Script:wght@600&display=swap" rel="stylesheet">
<style>
  :root {
    --purple-deep: #2f2158;
    --purple-mid: #4a3680;
    --purple-text: #3c2a6e;
    --purple-soft: #c9c2e2;
    --purple-dusk: #7a6ea8;
    --orange: #f7941d;
    --white: #ffffff;
    --glass-light: #eef3f8;
  }
  * { margin: 0; padding: 0; box-sizing: border-box; }
  html, body { width: 849px; height: 1200px; overflow: hidden; background: var(--white); }
  .cover {
    position: relative;
    width: 849px;
    height: 1200px;
    background: var(--white);
    overflow: hidden;
  }
  .artwork {
    position: absolute;
    left: 0;
    top: 560px;
    width: 849px;
    height: 640px;
    background:
      radial-gradient(ellipse 190px 200px at 235px 470px, rgba(247,148,29,0.35) 0%, rgba(247,148,29,0) 70%),
      radial-gradient(ellipse 200px 210px at 235px 470px, var(--glass-light) 0%, rgba(238,243,248,0) 100%),
      radial-gradient(ellipse 200px 210px at 620px 470px, var(--glass-light) 0%, rgba(238,243,248,0) 100%),
      linear-gradient(180deg, var(--white) 0%, var(--purple-soft) 45%, var(--purple-dusk) 100%);
  }
  .title-band {
    position: absolute;
    top: 0;
    left: 0;
    width: 849px;
    height: 560px;
  }
  .title {
    position: absolute;
    top: 28px;
    left: 0;
    width: 100%;
    text-align: center;
    font-family: "Alfa Slab One", "Rockwell", serif;
    font-weight: 400;
    text-transform: uppercase;
    color: var(--white);
    font-size: 76px;
    line-height: 114px;
    letter-spacing: 1px;
  }
  .title .accent { color: var(--orange); }
  .subtitle {
    position: absolute;
    top: 536px;
    width: 100%;
    text-align: center;
    font-family: "Source Sans 3", "Helvetica", sans-serif;
    color: var(--purple-text);
    font-size: 35px;
    line-height: 60px;
  }
  .subtitle .caps { text-transform: uppercase; }
  .credits {
    position: absolute;
    top: 668px;
    width: 100%;
    text-align: center;
    font-family: "Source Sans 3", "Helvetica", sans-serif;
    color: var(--orange);
    font-size: 21px;
    line-height: 38px;
  }
  .credits .name {
    font-family: "Dancing Script", cursive;
    font-size: 29px;
  }
</style>
</head>
<body>
  <main class="cover">
    <div class="artwork" role="img" aria-label="Photograph of a goldfish leaping from a crowded glass bowl of goldfish into an empty glass bowl beside it, on a soft purple backdrop"></div>

    <svg class="title-band" viewBox="0 0 849 560" aria-hidden="true">
      <defs>
        <linearGradient id="bandFill" x1="0" y1="0" x2="1" y2="1">
          <stop offset="0" stop-color="#56408f"/>
          <stop offset="1" stop-color="#2f2158"/>
        </linearGradient>
      </defs>
      <path d="M0 0 H849 V396 Q424.5 652 0 396 Z" fill="url(#bandFill)"/>
      <path d="M0 356 Q424.5 612 849 356" fill="none" stroke="#ffffff" stroke-width="3"/>
    </svg>

    <h1 class="title">
      Standing Tall<br>
      Won’t Require<br>
      Standing<br>
      <span class="accent">Alone</span>
    </h1>

    <p class="subtitle">
      How Trusting Your Own <span class="caps">Instincts</span><br>
      Can Shift Your Path and Build Your Venture
    </p>

    <p class="credits">
      By <span class="name">Marcia T. Vellby</span><br>
      With a Foreword by CEO <span class="name">Dorinda P. Halvorsen</span>
    </p>
  </main>
</body>
</html>
```